Fundraising Company Needs a Brochure Design

We need a brochure design for a company that helps charities raise money. Our main product is selling art on easels to raise money for various charites. The brochure will have a total of four pages with the size being 8.5" X 11" for each page. All of text will be provided for the brochure. The front page should include our logo and a short intro. The second page will contain a summary along with how the easel program works. The third page will contain information about the companies and charities we work with and other ways we raise money for charities. The back page will contain three testimonials along with our mission/vision statement and our contact information. We also need to include a picture of the easel somewhere in the catalog. The color of our logo is orange and light green but the brochure doesn't need to contain those colors.
Target Market(s)
The brochure will be presented to major charities and local businesses alike.
Industry/Entity Type
It Company
Look and feel

```html
<!DOCTYPE html>
<html lang="en">
<head>
<meta charset="utf-8">
<title>Easel Giving – Brochure Spread</title>
<link rel="stylesheet" href="https://fonts.googleapis.com/css2?family=Arimo:ital,wght@0,400;0,700;1,400&family=Dosis:wght@500;700&display=swap">
<style>
  :root{
    --stage:#3a3b3d;
    --paper:#ffffff;
    --orange:#f07a22;
    --green:#3f8a34;
    --lime:#9bc83a;
    --yellow:#f3d21c;
    --gold-dark:#8a6414;
    --gold:#c9992f;
    --gold-light:#f1d27a;
    --ink:#1d1d1d;
  }
  *{box-sizing:border-box;margin:0;padding:0}
  html,body{width:1200px;height:900px;overflow:hidden}
  body{background:var(--stage);position:relative;font-family:"Arimo",Arial,sans-serif;color:var(--ink)}

  .spread{position:absolute;left:28px;top:80px;width:1144px;height:740px;display:flex;box-shadow:0 18px 40px rgba(0,0,0,.45)}
  .page{position:relative;width:572px;height:740px;background:var(--paper);overflow:hidden}
  .page--back{border-right:1px solid #e2e2e2}

  /* back page */
  .section-title{position:absolute;left:36px;top:22px;font-family:"Dosis",sans-serif;font-weight:500;font-size:26px;color:var(--orange)}
  .testimonial{position:absolute;padding:22px;background:linear-gradient(135deg,var(--gold-light),var(--gold) 35%,var(--gold-dark) 60%,var(--gold-light) 85%,var(--gold));box-shadow:2px 3px 6px rgba(0,0,0,.25)}
  .testimonial__body{width:100%;height:100%;background:var(--paper);border:2px solid var(--gold-dark);padding:22px 18px;font-size:13px;line-height:1.35}
  .testimonial--a{left:26px;top:62px;width:230px;height:280px}
  .testimonial--b{left:300px;top:92px;width:250px;height:240px}
  .testimonial--c{left:300px;top:362px;width:250px;height:250px}

  .mission{position:absolute;left:38px;top:372px;width:228px}
  .brand-small{display:flex;align-items:center;gap:8px;font-family:"Dosis",sans-serif;font-weight:700;font-size:26px;color:var(--orange)}
  .brand-small__mark{width:22px;height:22px;background:var(--lime)}
  .mission__text{margin-top:14px;font-size:13.5px;line-height:1.3}

  .back-band{position:absolute;left:0;bottom:0;width:572px;height:130px}
  .back-band__name{position:absolute;left:62px;bottom:72px;font-size:24px;color:var(--green)}

  /* front page */
  .brand-large{position:absolute;right:34px;top:48px;display:flex;align-items:center;gap:14px;font-family:"Dosis",sans-serif;font-weight:700;font-size:58px;color:var(--orange)}
  .brand-large__mark{width:46px;height:46px;background:var(--lime)}
  .cover-image{position:absolute;left:0;top:0;width:572px;height:740px}
  .easel{position:absolute;left:86px;top:372px;width:150px;height:380px;background:linear-gradient(180deg,#6d5a2a 0%,#8b8a4a 35%,#3d3424 60%,#f4f1e6 62%,#e9e4d4 90%,#2b241a 100%);border:2px solid #4a3a1a}
  .intro-banner{position:absolute;left:236px;top:560px;width:380px;height:116px;background:var(--paper);border-top:3px solid var(--orange);border-bottom:3px solid var(--orange);transform:rotate(-12deg);transform-origin:left top;padding:16px 50px 0 14px;font-style:italic;font-size:14px;line-height:1.35;color:var(--green)}
</style>
</head>
<body>
<main class="spread">

  <section class="page page--back" aria-label="Back page">
    <h2 class="section-title">Testimonials</h2>

    <figure class="testimonial testimonial--a">
      <blockquote class="testimonial__body">Cum eat ommodita poruntis sincture nullo excearum volut eos accupta porem idi dolupta doluptionse sim faccuptas debit, suntur simus, tecesquas simporia dolupta eos asperferior a sust denimet, cum volupt</blockquote>
    </figure>
    <figure class="testimonial testimonial--b">
      <blockquote class="testimonial__body">Cum eat ommodita poruntis sincture nullo excearum volut eos accupta porem idi dolupta doluptionse sim faccuptas debit, suntur simus, teceaquas simporia dolupta eos asperferior a sust denimet, cum volupt</blockquote>
    </figure>
    <figure class="testimonial testimonial--c">
      <blockquote class="testimonial__body">Cum eat ommodita poruntis sincture nullo excearum volut eos accupta porem idi dolupta doluptionse sim faccuptas debit, suntur simus, teceaquas simporia dolupta eos asperferior a sust denimet, cum volupt</blockquote>
    </figure>

    <div class="mission">
      <div class="brand-small"><span class="brand-small__mark"></span>Easel Giving</div>
      <p class="mission__text">At Easel Giving, our mission is to provide our partners with an opportunity to improve their communities, and support charitable causes using our unique, creative, and non-invasive fundraising activities.</p>
    </div>

    <svg class="back-band" viewBox="0 0 572 130" role="img" aria-label="Glowing yellow and green abstract photo band">
      <defs>
        <linearGradient id="bandFill" x1="0" y1="0" x2="1" y2="1">
          <stop offset="0" stop-color="#f6e27a"/>
          <stop offset=".5" stop-color="#e9c83a"/>
          <stop offset="1" stop-color="#b9d24a"/>
        </linearGradient>
      </defs>
      <path d="M0 20 C150 10 330 60 572 50 L572 130 L0 130 Z" fill="url(#bandFill)"/>
      <path d="M0 20 C150 10 330 60 572 50" fill="none" stroke="#9bc83a" stroke-width="3"/>
    </svg>
    <p class="back-band__name">Easel Giving</p>
  </section>

  <section class="page page--front" aria-label="Front page">
    <svg class="cover-image" viewBox="0 0 572 740" role="img" aria-label="Glowing abstract gallery corridor in yellow, orange and green light">
      <defs>
        <linearGradient id="coverFill" x1="0" y1="0" x2="1" y2="1">
          <stop offset="0" stop-color="#f3b52a"/>
          <stop offset=".35" stop-color="#fbf2a8"/>
          <stop offset=".65" stop-color="#d9e24a"/>
          <stop offset="1" stop-color="#6fae2e"/>
        </linearGradient>
      </defs>
      <path d="M0 230 C120 190 260 260 572 300 L572 740 L0 740 Z" fill="url(#coverFill)"/>
    </svg>

    <div class="brand-large"><span class="brand-large__mark"></span>Easel Giving</div>

    <div class="easel" role="img" aria-label="Framed landscape painting on a wooden easel with a sealed bid auction sign"></div>

    <p class="intro-banner">It’s our families, our friends, and our neighbours that make communities beautiful. When we join together to help those amongst us in need, a beautiful community can become a work of art.</p>
  </section>

</main>
</body>
</html>
```